Custom unique Stationary design for Logistics company

We need a custom, unique , elegant and luxurious full stationary design using our new logo, following these guidelines:
1- Business card: double sided, both sides uses the navy blue as the background main color (same as the code of the navy blue used in our logo).
2- envelope and folder: also use the same navy blue as the main background color.
3- book cover( notepad cover) : same thing with the navy blue
4- letterhead: feel free to use the combination of the colors in our logo.
5- rest of the items are up to your creativity

Target Market(s)

corporates and other businesses

Industry/Entity Type

Logistics and heavy machines contractors

Requirements
Must have
• Letterhead, business card, envelope, notepad cover, paper, file
Nice to have
• navy blue to be main background color for business card, envelope, notepad cover

```html
<!DOCTYPE html>
<html lang="en">
<head>
<meta charset="utf-8">
<title>Norvan Freight Stationery</title>
<link href="https://fonts.googleapis.com/css2?family=Arimo:wght@400;700&display=swap" rel="stylesheet">
<style>
  :root{
    --navy:#004f74;
    --stripe:#3b7799;
    --orange:#f06032;
    --board:#acacac;
    --paper:#ffffff;
    --paper-grey:#f1f1f3;
    --ink:#333333;
    --muted:#8a8a8a;
    --rule:#b9b9b9;
  }
  *{box-sizing:border-box;margin:0;padding:0}
  html,body{width:724px;height:1200px;overflow:hidden;background:var(--board)}
  body{position:relative;font-family:"Arimo",Arial,sans-serif;color:var(--ink)}
  .piece{position:absolute;overflow:hidden;box-shadow:1px 2px 3px rgba(0,0,0,.28)}
  .header-band{position:absolute;left:0;top:0;width:100%;background:var(--navy);border-bottom:1px solid var(--orange)}
  .stripe{position:absolute;height:4px;background:var(--stripe)}
  .wordmark{position:absolute;display:flex;align-items:center;gap:4px;font-weight:700;color:#fff;white-space:nowrap;letter-spacing:.04em;transform:translate(-50%,-50%)}
  .wordmark .dot{border-radius:50%;background:var(--orange)}
  .contact-list{position:absolute;list-style:none;color:var(--muted)}
  .contact-list li{display:flex;align-items:center;gap:3px}
  .contact-list i{display:inline-block;border-radius:50%;background:var(--orange)}
  .address{position:absolute;text-align:right;color:var(--muted);list-style:none}

  /* business card */
  .card-front{left:110px;top:28px;width:244px;height:139px;background:linear-gradient(90deg,#f1f1f3,#fff)}
  .card-front .header-band{height:67px}
  .card-name{position:absolute;right:130px;top:93px;text-align:right}
  .card-name strong{display:block;color:var(--orange);font-size:8.5px;font-weight:700}
  .card-name span{display:block;color:var(--muted);font-size:7px;margin-top:1px}
  .card-divider{position:absolute;left:121px;top:90px;width:1px;height:25px;background:var(--rule)}
  .card-front .contact-list{left:128px;top:89px;font-size:6.5px;line-height:9.8px}
  .card-front .contact-list i{width:5px;height:5px}
  .card-back{left:376px;top:28px;width:245px;height:139px;background:var(--navy)}

  /* letterheads */
  .letterhead{top:191px;width:323px;height:457px;background:linear-gradient(100deg,#ececef,#fbfbfc 60%,#fff)}
  .letterhead .header-band{height:52px}
  .letter-body{position:absolute;left:29px;top:142px;width:266px;font-size:5.3px;line-height:6.6px;color:#3a3a3a}
  .letter-body h2{font-size:7.4px;font-weight:700;color:#333;margin-bottom:12px}
  .letter-body p{margin-bottom:6px}
  .letter-body .closing{font-size:4.2px;font-weight:700;margin-top:9px}
  .signature{position:absolute;left:29px;top:316px;width:56px;height:17px;background:linear-gradient(90deg,#dcdce0,#ececef);border-radius:3px}
  .footer-rule{position:absolute;left:25px;right:25px;top:409px;height:1px;background:var(--rule)}
  .letterhead .contact-list{left:25px;top:414px;font-size:5.5px;line-height:8.2px}
  .letterhead .contact-list i{width:4px;height:4px}
  .letterhead .address{right:25px;top:414px;font-size:5.5px;line-height:8.2px}
  .ruled-lines{position:absolute;left:31px;right:31px;top:90px;height:312px;background:repeating-linear-gradient(to bottom,transparent 0 12.5px,#c7c7c7 12.5px 13.5px);-webkit-mask:repeating-linear-gradient(90deg,#000 0 3px,transparent 3px 5px);mask:repeating-linear-gradient(90deg,#000 0 3px,transparent 3px 5px)}

  /* folder */
  .folder-outside{left:31px;top:672px;width:323px;height:228px;background:var(--navy)}
  .folder-outside .sheet{position:absolute;left:161px;top:0;width:162px;height:228px;background:linear-gradient(90deg,#cfcfd2,#f4f4f6 50%,#fff)}
  .folder-outside .sheet .header-band{height:26px}
  .mini-rule{position:absolute;left:12px;right:12px;top:205px;height:1px;background:var(--rule)}
  .folder-outside .contact-list{left:12px;top:208px;font-size:2.6px;line-height:4px}
  .folder-outside .contact-list i{width:2px;height:2px}
  .folder-outside .address{right:12px;top:208px;font-size:2.6px;line-height:4px}

  .folder-inside{left:31px;top:920px;width:323px;height:228px;background:linear-gradient(90deg,#f5f5f6,#fff 40%)}
  .folder-inside .inner-right{position:absolute;left:161px;top:0;width:162px;height:228px;background:#c4c4c6}
  .folder-inside .sheet{position:absolute;left:169px;top:12px;width:145px;height:200px;background:linear-gradient(110deg,#f7f7f8,#e6e6e8)}
  .folder-inside .sheet .header-band{height:24px}
  .mini-letter{position:absolute;left:13px;top:63px;width:120px;font-size:2.7px;line-height:3.6px;color:#555}
  .mini-letter h3{font-size:3.2px;font-weight:700;color:#333;margin-bottom:6px}
  .mini-letter p{margin-bottom:3px}
  .pockets{position:absolute;left:0;top:0}

  /* envelopes */
  .envelope-front{left:371px;top:672px;width:330px;height:143px;background:#fff}
  .envelope-front .header-band{height:46px}
  .return-address{position:absolute;left:112px;top:31px;color:#fff;font-size:4.6px;line-height:6px}
  .envelope-back{left:371px;width:330px;height:143px;background:linear-gradient(90deg,#ebebed,#fff 40%)}
  .envelope-back.white-flap{top:839px}
  .envelope-back.navy-flap{top:1004px}
  .envelope-back svg{position:absolute;left:0;top:0}
</style>
</head>
<body>

<!-- Business card, front -->
<section class="piece card-front" aria-label="Business card front">
  <div class="header-band">
    <div class="stripe" style="left:168px;right:0;top:23px"></div>
    <div class="stripe" style="left:0;width:74px;top:45px"></div>
    <div class="wordmark" style="left:122px;top:36px;font-size:13px"><span class="dot" style="width:6px;height:6px"></span>NORVAN FREIGHT</div>
  </div>
  <div class="card-name"><strong>MARCUS HALE</strong><span>Manager</span></div>
  <div class="card-divider"></div>
  <ul class="contact-list">
    <li><i></i>555-018-2740</li>
    <li><i></i>hello@norvanfreight.com</li>
    <li><i></i>www.norvanfreight.com</li>
  </ul>
</section>

<!-- Business card, back -->
<section class="piece card-back" aria-label="Business card back">
  <svg width="245" height="139" viewBox="0 0 245 139" aria-hidden="true">
    <polygon points="125,0 175,0 238,70 175,139 125,139 187,70" fill="#fff"/>
    <polygon points="175,0 245,0 245,139 175,139 238,70" fill="var(--orange)"/>
  </svg>
  <div class="wordmark" style="left:74px;top:70px;font-size:14px"><span class="dot" style="width:7px;height:7px"></span>NORVAN FREIGHT</div>
</section>

<!-- Letterhead with letter -->
<section class="piece letterhead" style="left:31px" aria-label="Letterhead">
  <div class="header-band">
    <div class="stripe" style="left:232px;right:0;top:18px"></div>
    <div class="stripe" style="left:0;width:92px;top:35px"></div>
    <div class="wordmark" style="left:161px;top:28px;font-size:13px"><span class="dot" style="width:6px;height:6px"></span>NORVAN FREIGHT</div>
  </div>
  <div class="letter-body">
    <h2>Dear Mr. Hale,</h2>
    <p>Lorem ipsum dolor sit amet, consectetuer adipiscing elit, sed diam nonmmy nibh euismod tincidunt ut laor eet dolore magna aliquam erat volutpat. Ut wisi enim ad minim veniam, quis nostrud exerci tationmcorper suscipit lobortis nisl ut aliquip ex ea commodo consequat. Duis autem vel eum iriure dolor in hendrerit in vulputate velit esse molestie consequat, vel illum dolore eu feugiat</p>
    <p>Rorem ipsum dolor sit amet, consectetuer adipiscing elit, sed diam nonmmy nibh euismod tincidunt ut laor eet dolore magna aliquam erat volutpat. Ut wisi enim ad minim veniam, quis nostrud exerci tationmcorper suscipit lobortis nisl ut aliquip ex ea commodo consequat. Duis autem vel eum iriure dolor in hendrerit in vulputate velit esse molest</p>
    <p>Dorem ipsum dolor sit amet, consectetuer adipiscing elit, sed diam nonmmy nibh euismod tincidunt ut laor eet dolore magna aliquam erat volutpat. Ut wisi enim ad minim veniam, quis nostrud exerci tationmcorper suscipit lobortis nisl ut aliquip ex ea commodo consequat. Duis autem vel eum iriure dolor in hendrerit in suscipit lobortis nisl ut aliquip ex ea commodo consequat. Duis autem vel eum iriure dolor in hendrerit in vulputate velit esse molestie consequat, vel illum</p>
    <p>Sorem ipsum dolor sit amet, consectetuer adipiscing elit, sed diam nonmmy nibh euismod tincidunt ut laor eet dolore magna aliquam erat volutpat. Ut wisi enim ad minim veniam, quis nostrud exerci tationmcorper suscipit lobortis nisl ut aliquip ex ea commodo consequat. Duis autem vel eum iriure dolor in</p>
    <p class="closing">Sincerely,</p>
  </div>
  <div class="signature" role="img" aria-label="Handwritten signature"></div>
  <div class="footer-rule"></div>
  <ul class="contact-list">
    <li><i></i>555-018-2740</li>
    <li><i></i>hello@norvanfreight.com</li>
    <li><i></i>www.norvanfreight.com</li>
  </ul>
  <ul class="address"><li>Your Address</li><li>City</li><li>State, Zip 0000</li></ul>
</section>

<!-- Ruled notepaper -->
<section class="piece letterhead" style="left:371px" aria-label="Ruled note paper">
  <div class="header-band">
    <div class="stripe" style="left:232px;right:0;top:18px"></div>
    <div class="stripe" style="left:0;width:92px;top:35px"></div>
    <div class="wordmark" style="left:161px;top:28px;font-size:13px"><span class="dot" style="width:6px;height:6px"></span>NORVAN FREIGHT</div>
  </div>
  <div class="ruled-lines"></div>
  <div class="footer-rule"></div>
  <ul class="contact-list">
    <li><i></i>555-018-2740</li>
    <li><i></i>hello@norvanfreight.com</li>
    <li><i></i>www.norvanfreight.com</li>
  </ul>
  <ul class="address"><li>Your Address</li><li>City</li><li>State, Zip 0000</li></ul>
</section>

<!-- Folder, outside -->
<section class="piece folder-outside" aria-label="Presentation folder outside">
  <div class="wordmark" style="left:80px;top:112px;font-size:12px"><span class="dot" style="width:6px;height:6px"></span>NORVAN FREIGHT</div>
  <div class="sheet">
    <div class="header-band">
      <div class="stripe" style="left:124px;right:0;top:9px;height:2px"></div>
      <div class="stripe" style="left:0;width:40px;top:18px;height:2px"></div>
      <div class="wordmark" style="left:81px;top:14px;font-size:7px"><span class="dot" style="width:3px;height:3px"></span>NORVAN FREIGHT</div>
    </div>
    <div class="mini-rule"></div>
    <ul class="contact-list">
      <li><i></i>555-018-2740</li>
      <li><i></i>hello@norvanfreight.com</li>
      <li><i></i>www.norvanfreight.com</li>
    </ul>
    <ul class="address"><li>Your Address</li><li>City</li><li>State, Zip 0000</li></ul>
  </div>
</section>

<!-- Folder, inside -->
<section class="piece folder-inside" aria-label="Presentation folder inside">
  <div class="inner-right"></div>
  <div class="sheet">
    <div class="header-band">
      <div class="stripe" style="left:110px;right:0;top:8px;height:2px"></div>
      <div class="stripe" style="left:0;width:36px;top:17px;height:2px"></div>
      <div class="wordmark" style="left:72px;top:13px;font-size:6.5px"><span class="dot" style="width:3px;height:3px"></span>NORVAN FREIGHT</div>
    </div>
    <div class="mini-letter">
      <h3>Dear Mr. Hale,</h3>
      <p>Thank you for choosing us for your heavy cargo needs. Our team will plan every route with care and keep you updated at each stage.</p>
      <p>Your equipment will be loaded, secured and delivered on schedule by trained crews using our own fleet.</p>
      <p>We look forward to working together.</p>
    </div>
  </div>
  <svg class="pockets" width="323" height="228" viewBox="0 0 323 228" aria-hidden="true">
    <path d="M0 132 H142 Q150 132 150 142 L161 228 H0 Z" fill="var(--navy)"/>
    <path d="M323 132 H181 Q171 132 170 142 L161 228 H323 Z" fill="var(--navy)"/>
  </svg>
</section>

<!-- Envelope, front -->
<section class="piece envelope-front" aria-label="Envelope front">
  <div class="header-band">
    <div class="stripe" style="left:106px;right:0;top:17px"></div>
    <div class="stripe" style="left:0;width:14px;top:32px"></div>
    <div class="wordmark" style="left:60px;top:25px;font-size:8px"><span class="dot" style="width:4px;height:4px"></span>NORVAN FREIGHT</div>
    <p class="return-address">Your Address, City<br>State, Zip 0000</p>
  </div>
</section>

<!-- Envelope, back with white flap -->
<section class="piece envelope-back white-flap" aria-label="Envelope back">
  <svg width="330" height="143" viewBox="0 0 330 143" aria-hidden="true">
    <path d="M1 0 H329 L322 30 Q318 40 306 40 H24 Q12 40 8 30 Z" fill="#fff" stroke="#d6d6d8" stroke-width=".8"/>
  </svg>
  <div class="wordmark" style="left:165px;top:19px;font-size:8px;color:var(--navy)"><span class="dot" style="width:4px;height:4px"></span>NORVAN FREIGHT</div>
</section>

<!-- Envelope, back with navy flap -->
<section class="piece envelope-back navy-flap" aria-label="Envelope back navy flap">
  <svg width="330" height="143" viewBox="0 0 330 143" aria-hidden="true">
    <path d="M0 0 H330 L322 30 Q318 39 306 39 H24 Q12 39 8 30 Z" fill="var(--navy)"/>
  </svg>
  <div class="wordmark" style="left:165px;top:19px;font-size:8px"><span class="dot" style="width:4px;height:4px"></span>NORVAN FREIGHT</div>
</section>

</body>
</html>
```